Dietitian/Nutritionist seeks trifold marketing brochure

We need a trifold brochure for marketing to patients within a doctors surgery. This will be a source of information for prospective patients, what they can expect and how to contact us. The brochure needs to have some key information such as a brief description of the services available, fees, locations of clinics and contact information. Our current brochure has been uploaded which has the information you need to complete this project. The files you provide will allow us to edit the information at a later date as pricing and services change.

Target Market(s)

Patients who have been referred to see a dietitian/nutritionist and people who are considering seeing a dietitian/nutritionist but haven't decided

Industry/Entity Type

Dietician

Font styles to use
Serif

Colors

Designer to choose colors to be used in the design.

Requirements
Must have
• My logo
• Chartered wellness nutritionist logo
• My website address and contact details
• Most of the information that is in my current brochure
• Locations/names of the four clinics
Nice to have
• Images that promote cooking, health and wellbeing

```html
<!DOCTYPE html>
<html lang="en">
<head>
<meta charset="utf-8">
<title>Riverbend Nutrition &amp; Dietetics – Trifold Front</title>
<link href="https://fonts.googleapis.com/css2?family=Source+Sans+3:wght@400;600;700&display=swap" rel="stylesheet">
<style>
  :root{
    --paper:#eef0f2;
    --stage:#e4e4e4;
    --navy:#0c3a8c;
    --navy-deep:#0e2a78;
    --sky:#1b86c8;
    --lime:#9cc41e;
    --lime-dark:#86ad12;
    --ink:#1c1f3a;
    --term:#1a3fa6;
    --orange:#f07a1c;
    --white:#ffffff;
  }
  *{box-sizing:border-box;margin:0;padding:0}
  html,body{width:1200px;height:1000px;overflow:hidden}
  body{background:var(--stage);font-family:"Source Sans 3",Arial,sans-serif;color:var(--ink);position:relative}
  .brochure{position:absolute;left:56px;top:32px;width:1089px;height:845px;background:var(--paper);overflow:hidden;box-shadow:0 2px 10px rgba(0,0,0,.15)}
  .backdrop{position:absolute;inset:0}
  .abs{position:absolute}

  .brand{display:flex;align-items:center;gap:8px}
  .brand-dot{border-radius:50%;background:var(--lime);flex:none}
  .brand-name{color:var(--navy);font-weight:600;line-height:1.05}
  .brand--left{left:86px;top:62px}
  .brand--left .brand-dot{width:48px;height:48px}
  .brand--left .brand-name{font-size:19px}
  .brand--mid{left:424px;top:230px}
  .brand--mid .brand-dot{width:66px;height:66px}
  .brand--mid .brand-name{font-size:24px}
  .brand--right{left:766px;top:44px}
  .brand--right .brand-dot{width:76px;height:76px}
  .brand--right .brand-name{font-size:27px}

  .services{left:51px;top:146px;width:278px;height:457px;background:var(--lime);border-radius:16px;padding:80px 18px 0 17px}
  .services-title{position:absolute;left:29px;top:2px;width:224px;height:56px;background:var(--navy-deep);color:var(--white);font-size:16px;line-height:19px;text-align:center;padding-top:9px;border-radius:0 0 4px 4px}
  .service-list{list-style:none;display:flex;flex-direction:column;gap:18px}
  .service-list li{position:relative;padding-left:14px;font-size:15.5px;line-height:18.5px;color:var(--ink)}
  .service-list li::before{content:"";position:absolute;left:0;top:6px;width:7px;height:7px;background:var(--navy-deep)}
  .term{color:var(--term)}

  .photo{border-radius:50%}
  .photo--bowl{left:62px;top:628px;width:260px;height:195px;border-radius:40% 40% 48% 48%;background:radial-gradient(circle at 45% 40%,#e84a2a,#f2a12a 45%,#e9d54a 70%,rgba(238,240,242,0) 72%)}
  .photo--portrait{left:372px;top:0;width:330px;height:330px;border-radius:0;background:radial-gradient(ellipse at 55% 40%,#c9c9c9,#dcdcdc 45%,rgba(238,240,242,0) 72%)}
  .photo--dairy{left:433px;top:550px;width:216px;height:216px;background:radial-gradient(circle at 40% 55%,#f4efe6 0 18%,#e7a0b2 28%,#d9462e 48%,#8bb83a 70%,#4a7a22)}
  .photo--fruit{left:724px;top:228px;width:360px;height:360px;background:radial-gradient(circle at 45% 40%,#a6cf3a 0 20%,#e23b2b 40%,#f4b21d 60%,#dfe6ee 78%,#cfd8e4)}

  .intro{left:420px;top:346px;width:256px;text-align:center;font-size:13.5px;line-height:16.5px;color:var(--ink)}
  .intro p+p{margin-top:16px}
  .web-mid{left:364px;top:786px;width:367px;text-align:center;color:#5fb7ea;font-size:15px}

  .contact-card{left:731px;top:624px;width:358px;text-align:center}
  .person{font-size:25px;font-weight:700;color:var(--navy-deep);letter-spacing:.2px}
  .role{display:inline-block;margin-top:3px;background:var(--navy-deep);color:var(--white);font-size:12px;padding:1px 8px}
  .contacts{list-style:none;margin-top:12px;font-size:13px;line-height:16.5px;color:var(--ink)}
  .contacts li{display:flex;justify-content:center;align-items:center;gap:4px}
  .contacts svg{width:11px;height:11px}
  .badge{left:852px;top:772px;width:97px;height:46px;background:var(--orange)}
</style>
</head>
<body>
<main class="brochure">
  <svg class="backdrop" viewBox="0 0 1089 845" width="1089" height="845" aria-hidden="true">
    <rect width="1089" height="845" fill="var(--paper)"/>
    <rect x="731" y="520" width="358" height="325" fill="var(--lime)"/>
    <path d="M364 845 L364 612 C470 585 600 560 680 500 C735 455 700 330 760 250 C820 175 960 150 1089 210 L1089 520 L731 520 L731 845 Z" fill="var(--navy)"/>
    <circle cx="904" cy="408" r="206" fill="var(--navy)"/>
    <path d="M0 700 C120 655 250 628 364 612 L364 690 C250 690 120 715 0 770 Z" fill="var(--sky)"/>
    <circle cx="541" cy="658" r="116" fill="var(--sky)"/>
  </svg>

  <div class="abs photo photo--portrait" role="img" aria-label="Faded photo of a smiling woman holding a bowl of fresh fruit"></div>

  <div class="abs brand brand--left"><span class="brand-dot"></span><span class="brand-name">Riverbend<br>Nutrition &amp; Dietetics</span></div>

  <section class="abs services">
    <h2 class="services-title" style="font-weight:400">A Chartered Wellness<br>Nutritionist can assist you with:</h2>
    <ul class="service-list">
      <li><span class="term">Diabetes</span> - Impaired Glucose Tolerance, Type 1 &amp; 2 Diabetes, Gestational Diabetes</li>
      <li><span class="term">Digestive</span> - Health Irritable Bowel Syndrome, Coeliac Disease, Diverticular Disease</li>
      <li><span class="term">Gastric banding</span> and other surgical methods of weight loss</li>
      <li><span class="term">Cardiovascular</span> - High cholesterol, High Blood Pressure, Risk Reduction</li>
      <li><span class="term">Weight Management</span> - loss/gain and support</li>
      <li><span class="term">General</span> Healthy Eating &amp; Nutrition</li>
    </ul>
  </section>

  <div class="abs photo photo--bowl" role="img" aria-label="Photo of a bowl of apples and citrus fruit wrapped in measuring tape"></div>

  <div class="abs brand brand--mid"><span class="brand-dot"></span><span class="brand-name">Riverbend<br>Nutrition &amp; Dietetics</span></div>

  <div class="abs intro">
    <p>Helping you to meet your individual nutrition goals with an emphasis on practical skills, everyday foods, and providing you with up to date advice.</p>
    <p>We work together to develop personalised eating plans that take into consideration your food preferences, health, work, family and lifestyle needs.</p>
  </div>

  <div class="abs photo photo--dairy" role="img" aria-label="Photo of a glass of milk and a bowl of yoghurt surrounded by fruit and vegetables"></div>
  <div class="abs web-mid">www.riverbenddietitian.com.au</div>

  <div class="abs brand brand--right"><span class="brand-dot"></span><span class="brand-name">Riverbend<br>Nutrition &amp; Dietetics</span></div>

  <div class="abs photo photo--fruit" role="img" aria-label="Photo of a glass bowl of grapes, apples and bananas beside salad, berries and orange juice"></div>

  <section class="abs contact-card">
    <h1 class="person">DANIEL ASHWORTH</h1>
    <span class="role">Chartered Wellness Nutritionist &amp; Chef</span>
    <ul class="contacts">
      <li><svg viewBox="0 0 12 12"><circle cx="6" cy="6" r="5.3" fill="none" stroke="var(--navy)" stroke-width="1"/><path d="M4 3.5 L5 3.3 L5.4 5 L4.8 5.4 C5.2 6.3 5.8 6.9 6.6 7.2 L7 6.6 L8.6 7 L8.5 8 C6 8.3 3.7 6 4 3.5Z" fill="var(--navy)"/></svg>0400 512 736</li>
      <li><svg viewBox="0 0 12 12"><rect x="1" y="3" width="10" height="7" fill="none" stroke="var(--navy)"/><path d="M1 3 L6 7 L11 3" fill="none" stroke="var(--navy)"/></svg>daniel.a.nutrition@example.com</li>
      <li><svg viewBox="0 0 12 12"><circle cx="6" cy="6" r="5" fill="none" stroke="var(--navy)"/><ellipse cx="6" cy="6" rx="2.2" ry="5" fill="none" stroke="var(--navy)"/><path d="M1 6 H11" stroke="var(--navy)"/></svg>www.riverbenddietitian.com.au</li>
      <li><svg viewBox="0 0 12 12"><path d="M1 4 C3 2 9 2 11 4 L10 5.5 L8 5 L8 4 H4 L4 5 L2 5.5 Z" fill="var(--navy)"/><rect x="2.5" y="6" width="7" height="4.5" fill="var(--navy)"/></svg>6300 4172</li>
    </ul>
  </section>

  <div class="abs badge" role="img" aria-label="Professional accreditation badge"></div>
</main>
</body>
</html>
```